Business card design needed

We need a new business card design to re launch my carpentry business. Could include double sided card with list of services provided.
Kitchens, bathrooms, decks, pergolas, window replacements, timber floor installation, owner builder assistance and general carpentry.
Would like an eye catching card that becons to be read in bright colors that has a logo that could be also used on clothing vehicle sinage etc
Preferably in blues and reds we live near beach so maybe some type of Beecher feel
Target Market(s)
The target market of my business would be mainly individuals requiring professional carpentry services not just a handy man. The renovation market plays a big part of my business
Industry/Entity Type
Carpentry
Contact Information for Business Card
Carpenter & joiner
Mel Hartigan
Inverloch
lorika_mel@quellpost.com
0493816025
Look and feel

```html
<!DOCTYPE html>
<html lang="en">
<head>
<meta charset="utf-8">
<title>Services We Provide – Business Card Back</title>
<link rel="stylesheet" href="https://fonts.googleapis.com/css2?family=Orbitron:wght@400&family=Share+Tech&family=Comfortaa:wght@300&display=swap">
<style>
  :root {
    --page-white: #ffffff;
    --ocean-blue: #2f4f9e;
    --lagoon-teal: #06a1b6;
    --text-white: #ffffff;
    --watermark-tint: rgba(255, 255, 255, 0.16);
  }
  html, body {
    margin: 0;
    padding: 0;
    width: 1200px;
    height: 714px;
    overflow: hidden;
    background: var(--page-white);
  }
  .card {
    position: absolute;
    left: 18px;
    top: 0;
    width: 1180px;
    height: 714px;
    overflow: hidden;
    background: var(--lagoon-teal);
  }
  .card__top-band {
    position: absolute;
    left: 0;
    top: 0;
    width: 100%;
    height: 424px;
    background: var(--ocean-blue);
  }
  .card__tagline-mark {
    position: absolute;
    left: 40px;
    top: 600px;
    margin: 0;
    font-family: "Comfortaa", sans-serif;
    font-weight: 300;
    font-size: 128px;
    color: var(--watermark-tint);
    white-space: nowrap;
    transform-origin: 0 0;
    transform: rotate(-30deg);
    letter-spacing: 2px;
  }
  .services {
    position: absolute;
    left: 0;
    top: 0;
    width: 100%;
    text-align: center;
    color: var(--text-white);
  }
  .services__title {
    margin: 84px 0 0;
    font-family: "Orbitron", sans-serif;
    font-weight: 400;
    font-size: 58px;
    letter-spacing: 4px;
    line-height: 1.2;
    text-decoration: underline;
    text-decoration-thickness: 3px;
    text-underline-offset: 8px;
  }
  .services__list {
    margin: 62px 0 0;
    font-family: "Share Tech", sans-serif;
    font-size: 46px;
    line-height: 65px;
    letter-spacing: 0.5px;
  }
</style>
</head>
<body>
  <main class="card">
    <div class="card__top-band"></div>
    <p class="card__tagline-mark">Carpenter &amp; joiner</p>
    <section class="services">
      <h1 class="services__title">Services We Provide</h1>
      <p class="services__list">
        Kitchens, bathrooms, decks, pergolas,<br>
        window replacements,<br>
        timber floor installation,<br>
        owner builder assistance<br>
        and general carpentry.
      </p>
    </section>
  </main>
</body>
</html>
```